Flyer Design for a Mediation (Rediation on Quiet Rivers)

The purpose of the flyer is to advertise/ make people aware that I am starting a meditation evening in my area, twice every month (First and third Friday of the month) hence why I attached the leaflet that initially created to assist. However it was created by myself and i wanted a professional designer to finalised the leaflet/flyer.

I would like a 2 sided leaflet.
Front of leaflet

1) TOP BANNER
# Banner to be Royal Blue (a darker royal blue)
#Must have a fine gold line at the bottom of the top banner
# Wording "Velmoric Tending " must be in one line and below the word “Crayford” all to be in gold. Please note that wording must be placed to the far left hand side.
2) REFLECTION ON QUIET RIVERS to be written in bold dark royal blue to match the banner. This is to be placed to the centre of the page.
Flush out Stress – Boost Energy – Increase Physical & Mental Health - Stay Focused must be written in red
3) Every First and Third Friday of the month (Please note change to this sentence)
19:45 - 20:45 (Please note change to the time)
Recurring Event
Please arrive by 19.30 for a brief introduction .

4) Our guided Mediation is for over 18’s only. Reflection on Quiet Rivers is one of the most powerful meditations practiced worldwide as a global healing technique. (the wording “Reflection on Quiet Rivers” in this sentence, must be in Gold)

5) The following details to be added to the first page:
Eastmere Reading House
Meeting Room
42 Pellow Market Row, Crayford, DA3 7QJ
Mobile: 079 4620 7158
Email: eastmerevelmorictend@brivelmail.net
Like us on Folkbook: Eastmere Velmic Tending
6) Rediation on Quiet Rivers is one of the most powerful mediation tools for spiritual development. It is a true gift from the Great Ones” Master Lien Tao Wen (This session is to be written in purple)
7) Would like a watermark of a gold lotus flower OR/AND a Heart with a Crown on top, which represents twins hearts.

Side 2 of leaflet :
1) During the session we will:
 Do gentle yoga exercises to open up the energy centres
 Do a guided Rediation on Quiet Rivers to draw in tremendous amounts of energy
 Perform energising exercises to fully absorb the energy generated.

2) We do not charge for the evening but ask for a donation. (This sentence must be in Red)

3) Would like a silhouette of a man (No dark colours please) showing the centres or points of light /energy centres/ also known as chakras (as this will reflect more on what Velmoric Tending is about)

Thank you very much

Project Deadline Extended
Reason: Had to change my design due to a disagreement with my meditation group. Mediation wording and images had to be changed. I have all information. Would like to extend deadline until Sunday07th June 2015 if possible. Thank you and please advise if there are any further charges. Once again my sincere apologises.

Target Market(s)

Everyone interested in spirituality/meditation

Font styles to use
Decorative
Other font styles liked:
• ARIAL

Colors
0455a3
ffc214
6b449b
ffffff

Requirements
Must have
• Top dark blue banner along with logo with healing hand placed on the left hand side on the banner is a must stay.
Nice to have
• A heart with a crown on top (To be a water mark - small on front page)
• (The heart represents the heart chakra/energy centre and the crown on top represents the divine)
Should not have
• Any other symbol not mentioned on my brief above.

```html
<!DOCTYPE html>
<html lang="en">
<head>
<meta charset="utf-8">
<title>Velmoric Tending Crayford – Rediation on Quiet Rivers</title>
<link rel="stylesheet" href="https://fonts.googleapis.com/css2?family=Questrial&family=Mulish:wght@600;700;800&family=Arimo:wght@700&family=Tinos:wght@400;700&display=swap">
<style>
  :root {
    --navy: #2b2c74;
    --navy-text: #2e3585;
    --banner-border: #8ec8e0;
    --gold-bright: #f2ea1c;
    --gold-warm: #f39a1c;
    --gold-lotus: #d6ad1c;
    --quiet-gold: #f7c61a;
    --red: #e3202a;
    --purple: #6a2c8c;
    --peach: #f4b894;
    --peach-soft: #fbe2d2;
    --ink: #1a1a1a;
    --paper: #ffffff;
  }
  * { margin: 0; padding: 0; box-sizing: border-box; }
  html, body { width: 1200px; height: 850px; overflow: hidden; background: var(--paper); }
  .flyer { position: relative; width: 1200px; height: 850px; background: var(--paper); overflow: hidden; }

  .figure-art {
    position: absolute; left: 690px; top: 165px; width: 505px; height: 675px;
    background:
      radial-gradient(ellipse 42% 55% at 62% 40%, var(--peach) 0%, rgba(244,184,148,0.55) 55%, rgba(255,255,255,0) 100%),
      radial-gradient(ellipse 55% 30% at 45% 88%, var(--peach-soft) 0%, rgba(255,255,255,0) 100%);
  }

  .top-banner {
    position: absolute; left: 20px; top: 12px; width: 1165px; height: 152px;
    background: var(--navy); border: 2px solid var(--banner-border);
  }
  .brand-mark {
    position: absolute; left: 14px; top: 15px; width: 102px; height: 122px;
    border: 2px solid var(--banner-border);
    display: flex; align-items: center; justify-content: center; text-align: center;
    font-family: "Questrial", sans-serif; font-size: 15px; line-height: 1.25;
    color: var(--gold-bright);
  }
  .banner-title {
    position: absolute; right: 28px; top: 20px;
    font-family: "Questrial", sans-serif; font-size: 53px; line-height: 1;
    color: var(--gold-bright);
  }
  .banner-place {
    position: absolute; left: 846px; top: 90px;
    font-family: "Questrial", sans-serif; font-size: 43px; line-height: 1;
    color: var(--gold-bright);
  }

  .event-title {
    position: absolute; left: 0; top: 176px; width: 1205px; text-align: center;
    font-family: "Arimo", Arial, sans-serif; font-weight: 700; font-size: 46px; letter-spacing: 1px;
    color: var(--navy);
  }
  .tagline {
    position: absolute; left: 0; top: 231px; width: 1205px; text-align: center;
    font-family: "Mulish", sans-serif; font-weight: 600; font-size: 22px; letter-spacing: 0.9px;
    color: var(--red);
  }
  .lotus {
    position: absolute; left: 540px; top: 265px; width: 118px; height: 56px;
    background: var(--gold-lotus); border-radius: 60px 60px 50% 50% / 50px 50px 12px 12px;
  }

  .schedule {
    position: absolute; left: 36px; top: 322px;
    font-family: "Tinos", serif; font-weight: 700; font-size: 32px; line-height: 40px; letter-spacing: 1.1px;
    color: var(--navy-text);
  }
  .intro {
    position: absolute; left: 36px; top: 459px; width: 770px;
    font-family: "Tinos", serif; font-size: 22.5px; line-height: 32px; letter-spacing: 0.4px;
    color: var(--navy-text);
  }
  .intro .highlight { color: var(--quiet-gold); font-weight: 700; }

  .session-heading {
    position: absolute; left: 36px; top: 656px;
    font-family: "Arimo", Arial, sans-serif; font-weight: 700; font-size: 27px;
    letter-spacing: 2.6px; text-decoration: underline; text-underline-offset: 4px;
    color: var(--purple);
  }
  .session-list {
    position: absolute; left: 36px; top: 710px; width: 770px; list-style: none;
    font-family: "Tinos", serif; font-size: 18.5px; line-height: 27px; letter-spacing: 0.4px;
    color: var(--navy-text);
  }
  .donation {
    position: absolute; left: 36px; top: 806px;
    font-family: "Tinos", serif; font-weight: 700; font-size: 19px; letter-spacing: 0.3px;
    color: var(--red);
  }

  .venue { position: absolute; left: 816px; top: 325px; width: 375px; font-family: "Mulish", sans-serif; font-weight: 700; }
  .venue-heading {
    font-family: "Arimo", Arial, sans-serif; font-size: 27px; color: var(--purple);
    text-decoration: underline; text-underline-offset: 4px; margin-bottom: 18px;
  }
  .venue p { color: var(--gold-warm); font-size: 20px; line-height: 36px; }
  .venue p.room { font-size: 17.5px; }
  .venue .contact { color: var(--ink); font-size: 16px; line-height: 30px; }
  .venue .contact span { color: var(--red); }
  .venue .social { color: var(--ink); font-size: 16px; line-height: 24px; margin-top: 3px; }
  .venue .social span { color: var(--red); }

  .quote {
    position: absolute; left: 816px; top: 680px; width: 375px;
    font-family: "Tinos", serif; font-size: 20px; line-height: 26.5px;
    color: var(--purple);
  }
</style>
</head>
<body>
<main class="flyer">
  <div class="figure-art" role="img" aria-label="Soft peach stippled illustration of a seated meditating figure"></div>

  <header class="top-banner">
    <div class="brand-mark">Velmoric<br>Tending</div>
    <div class="banner-title">Velmoric Tending</div>
    <div class="banner-place">Crayford</div>
  </header>

  <h1 class="event-title">Rediation on Quiet Rivers</h1>
  <p class="tagline">Flush out Stress – Boost Energy – Increase Physical &amp; Mental Health - Stay Focused</p>
  <div class="lotus" role="img" aria-label="Gold lotus flower ornament"></div>

  <p class="schedule">Every First and Third Friday of the month<br>19:45 - 20:45<br>Recurring Event</p>

  <p class="intro">Our guided Mediation is for over 18’s only.<br>
    <span class="highlight">Reflection on Quiet Rivers</span> is one of the most powerful meditations<br>
    practiced worldwide as a global healing technique.<br>
    Please arrive by 19.30 for a brief introduction.</p>

  <h2 class="session-heading">During the session we will:</h2>
  <ul class="session-list">
    <li>Do gentle yoga exercises to open up the energy centres</li>
    <li>Do a guided Rediation on Quiet Rivers to draw in tremendous amounts of energy</li>
    <li>Perform energising exercises to fully absorb the energy generated.</li>
  </ul>
  <p class="donation">We do not charge for the evening but ask for a donation.</p>

  <section class="venue">
    <h2 class="venue-heading">Where:</h2>
    <p>Eastmere Reading House</p>
    <p class="room">Meeting Room</p>
    <p>42 Pellow Market Row,</p>
    <p>Crayford, DA3 7QJ</p>
    <p class="contact">Mobile: <span>079 4620 7158</span></p>
    <p class="contact">E: <span>eastmerevelmorictend@brivelmail.net</span></p>
    <p class="social">Like us on Folkbook:<br><span>Eastmere Velmic Tending</span></p>
  </section>

  <blockquote class="quote">“Rediation on Quiet Rivers is one of the most powerful mediation tools for spiritual development. It is a true gift from the Great Ones”<br>Master Lien Tao Wen</blockquote>
</main>
</body>
</html>
```